Start Up Business Launcher needs a business card

We need a business card logo and word design for a new company called Varnick Ventures. We are a company dedicated to creating, testing, and developing, a myriad of repeatable and scalable business models (start ups) through innovative and consistent application of knowledge and expertise.

Target Market(s)

We test the marketability of start ups to various clientelle

Industry/Entity Type

Startup

Contact Information for Business Card

Varnick Ventures
Marcus Tellby LL.B, MBA.
Founder and President
#507 482 29 Ave SW Calgary AB
varnickventures@mailvista.example
(403) 821-3907

Colors

Designer to choose colors to be used in the design.

Requirements
Must have
• A logo for Varnick Ventures and a stylized written logo for Varnick Ventures
Nice to have
• bold design that demonstrates professionalism, consistency, and innovation.

```html
<!DOCTYPE html>
<html lang="en">
<head>
<meta charset="utf-8">
<title>Varnick Ventures — Business Card</title>
<link rel="stylesheet" href="https://fonts.googleapis.com/css2?family=Montserrat:wght@600&family=Roboto+Condensed:wght@400;700&display=swap">
<style>
  :root {
    --page-bg: #ececed;
    --front-bg: #0c1c2a;
    --front-ink: #e4e7ea;
    --back-bg: #9da3a9;
    --back-ink: #3d4852;
    --back-word: #59636c;
    --rule: #4a545d;
  }
  * { margin: 0; padding: 0; box-sizing: border-box; }
  html, body {
    width: 1200px; height: 1000px; overflow: hidden;
    background: var(--page-bg);
  }
  .card {
    position: absolute;
    left: 322px;
    width: 556px; height: 320px;
    border-radius: 22px;
    overflow: hidden;
  }
  .card--front { top: 110px; background: var(--front-bg); }
  .card--back  { top: 510px; background: var(--back-bg); }

  .brand {
    position: absolute; inset: 0;
    display: flex; flex-direction: column; align-items: center; justify-content: center;
    font-family: "Montserrat", sans-serif; font-weight: 600;
    color: var(--front-ink); line-height: 1.05; text-align: center;
  }
  .brand__name { font-size: 44px; letter-spacing: -1px; }
  .brand__sub { font-size: 24px; letter-spacing: 2px; text-transform: uppercase; }

  .holder {
    position: absolute; left: 58px; top: 52px;
    font-family: "Roboto Condensed", sans-serif; color: var(--back-ink);
  }
  .holder__name { font-size: 18px; font-weight: 700; }
  .holder__creds { font-size: 11px; font-weight: 400; margin-left: 2px; }
  .holder__role { font-size: 10px; margin-top: 1px; }

  .contact {
    position: absolute; right: 50px; top: 118px;
    padding-right: 10px;
    border-right: 2px solid var(--rule);
    font-family: "Roboto Condensed", sans-serif; color: var(--back-ink);
    font-size: 13px; line-height: 18px; text-align: right;
  }
  .contact__phone { font-weight: 700; }

  .back-word {
    position: absolute; left: 6px; bottom: -46px;
    font-family: "Montserrat", sans-serif; font-weight: 600;
    font-size: 140px; letter-spacing: -5px; line-height: 1;
    color: var(--back-word); white-space: nowrap;
  }
</style>
</head>
<body>
  <section class="card card--front">
    <div class="brand">
      <span class="brand__name">Varnick</span>
      <span class="brand__sub">Ventures</span>
    </div>
  </section>

  <section class="card card--back">
    <div class="holder">
      <p class="holder__name">Marcus Tellby <span class="holder__creds">LL.B, MBA.</span></p>
      <p class="holder__role">Founder and President</p>
    </div>
    <address class="contact" style="font-style:normal">
      <p>#507 482 29 Ave SW Calgary AB</p>
      <p>varnickventures@mailvista.example</p>
      <p class="contact__phone">(403) 821 - 3907</p>
    </address>
    <div class="back-word" aria-hidden="true">Varnick</div>
  </section>
</body>
</html>
```